Improving a camping website homepage header*

My client is very happy with his new website and its new functionalities. However, he's not very happy about the homepage design. Specifically, the header(this includes the menu, large header image and two columns beneath that). You can find the website here: http://lnkvo.example/siteTentra .

He forwarded me several other websites he likes. Which can be found in the attachments. I also included several pictures of the camping.

I'm looking for a design that will improve the header of the homepage with room for other global style chances. The logo cannot be changed.

Attachments
1) His old website homepage
2) Website mockup he liked.
3) Another website mockup he liked.

Other images can be found on the new website http://lnkvo.example/siteTentra or his old website http://lnkvo.example/formerSiteTentra.

Can you help us?
Updates

Hello guys. Here's a bit more information - Language used on the website is dutch. - The two columns left/right are supposed to link to Hire/Buy chalets. The client indicated that he finds these links important, but doesn't like the current design. I think this is partially the case because he doesn't like the icons. I'm looking forward to your designs!

Target Market(s)

30-50 year old wealthy people that want to purchase or rent cabins in the Netherlands.

Number of Pages Required

1 page

Colors

Designer to choose colors to be used in the design.

Requirements
Must have
• Improved header
Nice to have
• Global style changes
Should not have
• Logo changes

```html
<!DOCTYPE html>
<html lang="nl">
<head>
<meta charset="utf-8">
<title>Parc Veldhoeve – Huren &amp; Kopen</title>
<link rel="stylesheet" href="https://fonts.googleapis.com/css2?family=Lato:wght@300;400;700&display=swap">
<style>
:root{
  --green:#6aaf2a;
  --orange:#e07a1b;
  --dark:#1c1a18;
  --text:#444;
  --muted:#777;
  --card:#f1f1f1;
  --white:#fff;
}
*{box-sizing:border-box;margin:0;padding:0}
html,body{width:1200px;height:2723px;overflow:hidden}
body{position:relative;font-family:'Lato',sans-serif;color:var(--text);background:var(--white)}
.abs{position:absolute}
svg{display:block}

/* top bar */
.topbar{left:0;top:0;width:1200px;height:49px;background:var(--green)}
.contact-item{top:6px;display:flex;align-items:center;gap:18px;color:var(--white)}
.contact-item .ic{width:30px;height:30px;border-radius:50%;background:var(--white);display:flex;align-items:center;justify-content:center}
.contact-item b{display:block;font-size:12px;letter-spacing:1px;font-weight:700;line-height:16px}
.contact-item span{font-size:15px;line-height:18px}
.login{left:1011px;top:0;width:102px;height:49px;background:var(--orange);color:var(--white);font-size:13px;font-weight:700;display:flex;align-items:center;justify-content:center;letter-spacing:.5px}

/* nav */
.nav a{position:absolute;top:96px;font-size:12.5px;color:#333;text-decoration:none;letter-spacing:.4px;transform:translateX(-50%);white-space:nowrap}
.nav a.active{color:var(--orange)}
.nav a.active::after{content:"";position:absolute;left:-6px;right:-6px;top:26px;height:2px;background:var(--orange)}
.brand{left:514px;top:68px;display:flex;align-items:center;gap:12px}
.brand .mark{width:40px;height:40px;border-radius:50%;background:var(--green)}
.brand .name{font-size:29px;font-weight:400;color:var(--green);line-height:1}

/* hero */
.hero{left:0;top:167px;width:1200px;height:517px;background:linear-gradient(180deg,#3b3a30 0%,#4b3b32 45%,#3a2a24 80%,#2d2a22 100%)}
.hero-title{left:0;width:1200px;top:364px;text-align:center;color:var(--white);font-weight:300;font-size:54px;letter-spacing:1px}
.hero-sub{left:0;width:1200px;top:440px;display:flex;justify-content:center;align-items:center;gap:16px}
.hero-sub i{display:block;width:146px;height:2px;background:var(--white)}
.hero-sub span{color:var(--orange);font-weight:700;font-size:25px;letter-spacing:1px}
.hero-arrow{width:36px;height:36px;display:flex;align-items:center;justify-content:center}
.hero-arrow.prev{left:36px;top:408px;background:var(--orange)}
.hero-arrow.next{left:1128px;top:408px;border:2px solid var(--white)}
.dots{display:flex;gap:14px;align-items:center}
.dots i{display:block;width:9px;height:9px;border-radius:50%;background:#fff}
.dots i.on{width:14px;height:14px;background:var(--orange);border:3px solid #fff}
.dots.grey i{background:#bbb}
.dots.grey i.on{background:var(--orange);border-color:#fff;box-shadow:0 0 0 1px #bbb}

/* choice cards */
.choice{top:735px;width:501px;height:323px;background:var(--card);text-align:center}
.choice .circle{position:absolute;left:201px;top:55px;width:98px;height:98px;border-radius:50%;background:var(--green);display:flex;align-items:center;justify-content:center}
.choice h3{position:absolute;top:167px;width:100%;font-size:18px;font-weight:700;color:#333;letter-spacing:.3px}
.choice p{position:absolute;left:90px;width:321px;top:197px;font-size:13px;line-height:19px;color:var(--muted)}

/* headings */
.section-title{left:0;width:1200px;text-align:center;font-size:28px;font-weight:400;color:var(--green)}
.section-title b{color:var(--orange)}

/* recent chalets */
.chalet-photo{left:85px;top:1158px;width:589px;height:372px;background:linear-gradient(180deg,#4a8fd0 0%,#88b6de 35%,#b07a3c 60%,#7a4d22 85%,#5d7a3a 100%)}
.badge-rent{left:111px;top:1180px;width:90px;height:41px;background:var(--orange);color:var(--white);font-size:17px;display:flex;align-items:center;justify-content:center}
.photo-bar{left:85px;top:1467px;width:589px;height:63px;background:rgba(20,20,20,.85);color:var(--white)}
.photo-bar span{position:absolute;left:26px;top:19px;font-size:21px}
.mini-arrows{display:flex;gap:4px}
.mini-arrows i{display:flex;width:25px;height:25px;align-items:center;justify-content:center;background:var(--orange)}
.mini-arrows i.w{background:var(--white)}
.chalet-info h2{left:724px;top:1183px;width:390px;font-size:20px;font-weight:700;color:#333;line-height:25px}
.chalet-info p{left:724px;top:1243px;width:390px;font-size:13.5px;line-height:19.5px;color:var(--muted)}
.spec-label{top:1335px;font-size:13px;color:var(--orange)}
.spec{top:1357px;display:flex;align-items:center;gap:12px}
.spec .num{width:24px;height:24px;border-radius:50%;background:#999;color:#fff;font-size:12px;display:flex;align-items:center;justify-content:center;font-weight:700}
.spec .pill{height:24px;padding:0 12px;border-radius:12px;background:#999;color:#fff;font-size:12px;display:flex;align-items:center;font-weight:700}
.divider{left:724px;top:1401px;width:390px;height:1px;background:#ddd}
.price{left:724px;top:1412px;color:var(--green)}
.price b{font-size:30px;font-weight:700}
.price span{font-size:14px;margin-left:8px}
.btn{left:724px;top:1459px;width:125px;height:42px;background:var(--orange);color:#fff;font-size:13px;display:flex;align-items:center;justify-content:center}
.act{top:1459px;width:36px;height:36px;border-radius:50%;background:var(--orange);display:flex;align-items:center;justify-content:center}

/* related work */
.related{left:0;top:1585px;width:1200px;height:388px;background:linear-gradient(180deg,#2d241c 0%,#3c2e22 50%,#221c16 100%)}
.work{top:1684px;width:325px;height:182px;border:3px solid var(--white)}

/* testimonials */
.avatar{left:556px;top:2077px;width:86px;height:86px;border-radius:50%;background:linear-gradient(180deg,#d8d8d8,#9a9a9a)}
.person{left:0;width:1200px;top:2169px;text-align:center;font-size:18px;font-weight:700;color:#333}
.quote{left:310px;width:580px;top:2197px;text-align:center;font-size:13.5px;line-height:20px;color:var(--muted)}

/* footer */
.footer{left:0;top:2354px;width:1200px;height:369px;background:linear-gradient(180deg,#1f1c19,#141210)}
.f-head{top:2392px;font-size:14px;font-weight:700;letter-spacing:.4px;color:var(--white)}
.f-row{left:85px;display:flex;gap:14px;font-size:13.5px;line-height:17px;align-items:flex-start;color:var(--white)}
.f-row svg{flex:none;margin-top:1px}
.thumb{left:350px;width:149px;height:82px}
.social{display:flex;align-items:center;gap:20px;font-size:13.5px;color:var(--white)}
.social i{display:block;width:36px;height:36px;border-radius:50%;background:#3a3835;position:relative}
.social i::after{content:"";position:absolute;left:14px;top:14px;width:8px;height:8px;border-radius:50%;background:#fff}
.f-line{left:85px;top:2659px;width:1028px;height:1px;background:#3a3835}
.copy{left:0;width:1200px;top:2680px;text-align:center;font-size:13px;color:var(--white)}
</style>
</head>
<body>

<!-- top bar -->
<div class="abs topbar"></div>
<div class="abs contact-item" style="left:86px">
  <div class="ic"><svg width="16" height="16" viewBox="0 0 24 24"><path fill="#6aaf2a" d="M6.6 10.8a15 15 0 006.6 6.6l2.2-2.2a1 1 0 011-.25 11 11 0 003.6.6 1 1 0 011 1V20a1 1 0 01-1 1A17 17 0 013 4a1 1 0 011-1h3.5a1 1 0 011 1c0 1.25.2 2.45.6 3.6a1 1 0 01-.25 1z"/></svg></div>
  <div><b>CALL US</b><span>0312 - 44 20 70</span></div>
</div>
<div class="abs contact-item" style="left:438px">
  <div class="ic"><svg width="16" height="16" viewBox="0 0 24 24"><path fill="#6aaf2a" d="M3 5h18v14H3z"/><path fill="none" stroke="#fff" stroke-width="2" d="M3 6l9 7 9-7"/></svg></div>
  <div><b>MAIL US</b><span>info@parcveldhoeve.nl</span></div>
</div>
<div class="abs login">LOGIN</div>

<!-- navigation -->
<nav class="nav">
  <a class="active" style="left:156px">HOME</a>
  <a style="left:233px">THE PARK</a>
  <a style="left:327px">FINANCING</a>
  <a style="left:418px">CHALETS</a>
  <a style="left:856px">OFFERS</a>
  <a style="left:940px">FACILITIES</a>
  <a style="left:1031px">CONTACT</a>
</nav>
<div class="abs brand"><div class="mark"></div><div class="name">Parc Veldhoeve</div></div>

<!-- hero -->
<div class="abs hero" role="img" aria-label="Foto van een houten chalet tussen hoge bomen"></div>
<div class="abs hero-title">PARC VELDHOEVE</div>
<div class="abs hero-sub"><i></i><span>RENT | BUY</span><i></i></div>
<div class="abs hero-arrow prev"><svg width="16" height="16" viewBox="0 0 16 16"><path d="M14 8H3M7 4L3 8l4 4" stroke="#fff" stroke-width="2" fill="none"/></svg></div>
<div class="abs hero-arrow next"><svg width="16" height="16" viewBox="0 0 16 16"><path d="M2 8h11M9 4l4 4-4 4" stroke="#fff" stroke-width="2" fill="none"/></svg></div>
<div class="abs dots" style="left:570px;top:646px"><i></i><i class="on"></i><i></i></div>

<!-- rent / buy -->
<div class="abs choice" style="left:85px">
  <div class="circle"><svg width="40" height="40" viewBox="0 0 24 24"><path fill="#fff" d="M12 3l10 9h-3v9h-5v-6h-4v6H5v-9H2z"/></svg></div>
  <h3>RENT A CHALET</h3>
  <p>Lorem ipsum dolor sit amet, consectetur adipiscing elit. Aenean euismod bibendum laoreet. Proin gravida dolor sit amet lacus accumsan et viverra justo commodo.</p>
</div>
<div class="abs choice" style="left:613px">
  <div class="circle"><svg width="46" height="46" viewBox="0 0 24 24"><rect x="2" y="6" width="20" height="12" rx="1" fill="none" stroke="#fff" stroke-width="2"/><circle cx="12" cy="12" r="3.2" fill="#fff"/><rect x="4.5" y="8.5" width="15" height="7" fill="none" stroke="#fff" stroke-width="1"/></svg></div>
  <h3>BUY A CHALET</h3>
  <p>Lorem ipsum dolor sit amet, consectetur adipiscing elit. Aenean euismod bibendum laoreet. Proin gravida dolor sit amet lacus accumsan et viverra justo commodo.</p>
</div>

<!-- recent chalets -->
<h2 class="abs section-title" style="top:1104px">RECENT <b>CHALETS</b></h2>
<div class="abs chalet-photo" role="img" aria-label="Foto van een blokhut van rondhout onder blauwe lucht"></div>
<div class="abs badge-rent">RENT</div>
<div class="abs photo-bar"><span>RECOMMENDED</span>
  <div class="mini-arrows" style="position:absolute;left:502px;top:19px">
    <i><svg width="10" height="10" viewBox="0 0 10 10"><path d="M7 1L3 5l4 4" stroke="#fff" stroke-width="2" fill="none"/></svg></i>
    <i class="w"><svg width="10" height="10" viewBox="0 0 10 10"><path d="M3 1l4 4-4 4" stroke="#e07a1b" stroke-width="2" fill="none"/></svg></i>
  </div>
</div>
<div class="chalet-info">
  <h2 class="abs">LOREM IPSUM DOLOR SIT AMET, CONSECTETUR ADIPISCING</h2>
  <p class="abs">Lorem ipsum dolor sit amet, consectetur adipiscing elit. Aenean euismod bibendum laoreet. Proin gravida dolor sit amet lacus accumsan et viverra justo commodo. Lorem ipsum dolor sit amet, consectetur adipiscing elit.</p>
</div>
<div class="abs spec-label" style="left:724px">Bedroom</div>
<div class="abs spec-label" style="left:849px">Bathroom</div>
<div class="abs spec-label" style="left:963px">Measurement</div>
<div class="abs spec" style="left:724px">
  <svg width="40" height="24" viewBox="0 0 40 24"><path d="M2 2v20M2 16h36v6M6 10h8v6M14 12h24v4" stroke="#999" stroke-width="2" fill="none"/></svg>
  <span class="num">1</span>
</div>
<div class="abs spec" style="left:849px">
  <svg width="28" height="24" viewBox="0 0 28 24"><path d="M2 10h24v4a8 8 0 01-8 8h-8a8 8 0 01-8-8zM6 10V4a2 2 0 014 0M8 22l-2 2M20 22l2 2" stroke="#999" stroke-width="2" fill="none"/></svg>
  <span class="num">2</span>
</div>
<div class="abs spec" style="left:963px">
  <svg width="26" height="24" viewBox="0 0 26 24"><path d="M3 21L21 3M3 3l18 18M6 6l2-2M18 18l2-2" stroke="#999" stroke-width="2" fill="none"/></svg>
  <span class="pill">105 000,00 M</span>
</div>
<div class="abs divider"></div>
<div class="abs price"><b>€ 350</b><span>Maand</span></div>
<div class="abs btn">Lees Meer</div>
<div class="abs act" style="left:969px"><svg width="18" height="18" viewBox="0 0 24 24"><path d="M12 21l-8-8a5 5 0 017-7l1 1 1-1a5 5 0 017 7z" stroke="#fff" stroke-width="2.2" fill="none"/></svg></div>
<div class="abs act" style="left:1022px"><svg width="18" height="18" viewBox="0 0 24 24"><circle cx="18" cy="5" r="3" fill="#fff"/><circle cx="6" cy="12" r="3" fill="#fff"/><circle cx="18" cy="19" r="3" fill="#fff"/><path d="M6 12l12-7M6 12l12 7" stroke="#fff" stroke-width="2"/></svg></div>
<div class="abs act" style="left:1074px"><svg width="18" height="18" viewBox="0 0 24 24"><path d="M12 3v18M3 12h18" stroke="#fff" stroke-width="3"/></svg></div>

<!-- related work -->
<div class="abs related" role="img" aria-label="Donkere achtergrondfoto van een houten chalet"></div>
<h2 class="abs section-title" style="top:1628px">RELATED <b>WORK</b></h2>
<div class="abs work" style="left:85px;background:linear-gradient(180deg,#cfd6d8,#6a4a3c 55%,#6d7a52)" role="img" aria-label="Foto van een bruin houten chalet"></div>
<div class="abs work" style="left:437px;background:linear-gradient(180deg,#6a4a30,#8a5a34 50%,#c25a4a 80%,#7a8a40)" role="img" aria-label="Foto van een chalet met bloembakken"></div>
<div class="abs work" style="left:790px;background:linear-gradient(180deg,#3f86c8,#8ab6dc 35%,#c9963e 60%,#8a7a3a)" role="img" aria-label="Foto van een blokhut onder blauwe lucht"></div>
<div class="abs mini-arrows" style="left:571px;top:1894px">
  <i><svg width="10" height="10" viewBox="0 0 10 10"><path d="M7 1L3 5l4 4" stroke="#fff" stroke-width="2" fill="none"/></svg></i>
  <i class="w"><svg width="10" height="10" viewBox="0 0 10 10"><path d="M3 1l4 4-4 4" stroke="#e07a1b" stroke-width="2" fill="none"/></svg></i>
</div>

<!-- testimonials -->
<h2 class="abs section-title" style="top:2017px">OUR <b>TESTIMONIALS</b></h2>
<div class="abs avatar" role="img" aria-label="Portretfoto van de klant"></div>
<div class="abs person">JANE DOE</div>
<p class="abs quote">Lorem ipsum dolor sit amet, consectetur adipiscing elit. Aenean euismod bibendum laoreet. Proin gravida dolor sit amet lacus accumsan et viverra justo commodo. Lorem ipsum dolor sit amet, consectetur adipiscing elit.</p>
<div class="abs dots grey" style="left:570px;top:2284px"><i></i><i class="on"></i><i></i></div>

<!-- footer -->
<footer class="abs footer" role="img" aria-label="Donkere achtergrondfoto van een chalet"></footer>
<h4 class="abs f-head" style="left:85px">CONTACT</h4>
<h4 class="abs f-head" style="left:350px">NIEUWE CHALETS</h4>
<h4 class="abs f-head" style="left:613px">SOCIALE MEDIA</h4>

<div class="abs f-row" style="top:2434px"><svg width="14" height="14" viewBox="0 0 24 24"><path fill="#fff" d="M1 4l7-2 8 3 7-2v17l-7 2-8-3-7 2z"/></svg><span>Lindelaan 14b<br>&nbsp;&nbsp;4211 KM Dorsveld</span></div>
<div class="abs f-row" style="top:2488px"><svg width="14" height="14" viewBox="0 0 24 24"><path fill="#fff" d="M6.6 10.8a15 15 0 006.6 6.6l2.2-2.2a1 1 0 011-.25 11 11 0 003.6.6 1 1 0 011 1V20a1 1 0 01-1 1A17 17 0 013 4a1 1 0 011-1h3.5a1 1 0 011 1c0 1.25.2 2.45.6 3.6a1 1 0 01-.25 1z"/></svg><span>0312 - 44 20 70</span></div>
<div class="abs f-row" style="top:2523px"><svg width="14" height="14" viewBox="0 0 24 24"><path fill="#fff" d="M6 2h10v6H6zM3 9h18v12H3z"/></svg><span>0312 - 44 31 85</span></div>
<div class="abs f-row" style="top:2558px"><svg width="14" height="14" viewBox="0 0 24 24"><path fill="#fff" d="M2 5h20v14H2z"/><path d="M2 6l10 7 10-7" stroke="#1f1c19" stroke-width="2" fill="none"/></svg><span>info@parcveldhoeve.nl</span></div>
<div class="abs f-row" style="top:2593px"><svg width="14" height="14" viewBox="0 0 24 24"><circle cx="12" cy="12" r="10" fill="#fff"/><path d="M8 11h8M8 14h5" stroke="#1f1c19" stroke-width="2"/></svg><span>parcVeldhoeveChat</span></div>

<div class="abs thumb" style="top:2436px;background:linear-gradient(180deg,#6a4a30,#8a5a34 55%,#c25a4a 80%,#7a8a40)" role="img" aria-label="Foto van een nieuw chalet met bloembakken"></div>
<div class="abs thumb" style="top:2537px;background:linear-gradient(180deg,#3f86c8,#8ab6dc 35%,#c9963e 65%,#8a7a3a)" role="img" aria-label="Foto van een nieuwe blokhut"></div>

<div class="abs social" style="left:613px;top:2438px"><i></i>Buurtplein</div>
<div class="abs social" style="left:788px;top:2438px"><i></i>Prikbord</div>
<div class="abs social" style="left:962px;top:2438px"><i></i>Tuimel</div>
<div class="abs social" style="left:613px;top:2490px"><i></i>Tjilp</div>
<div class="abs social" style="left:788px;top:2490px"><i></i>Kijkbuis</div>
<div class="abs social" style="left:962px;top:2490px"><i></i>Dribbel</div>
<div class="abs social" style="left:613px;top:2541px"><i></i>Zoekplus</div>
<div class="abs social" style="left:788px;top:2541px"><i></i>Filmhoek</div>
<div class="abs social" style="left:962px;top:2541px"><i></i>Feed</div>
<div class="abs social" style="left:613px;top:2594px"><i></i>Netwerker</div>
<div class="abs social" style="left:788px;top:2594px"><i></i>Fotomoment</div>
<div class="abs social" style="left:962px;top:2594px"><i></i>Netwerker</div>

<div class="abs f-line"></div>
<div class="abs copy">Copyright 2018 | Parc Veldhoeve</div>

</body>
</html>
```